Design Mobile & Web App UI Mockup / Prototype

Hi, I've upload more details screens. As we are close to the deadline, please update your submission with these screens. It's important to focus on the mobile app, the website is not very important right now.

As the original contest. I need mockup for android and Ios app. We will developp two apps (one for customers, one for agents). Some screens are basically the same for the both. If the designer have others skills, he will hire to work on the project.

The designer will provide all the image, vector, set color code, fonts, pages description etc for the developer. I have attached an example of the logo with white color if your designs have dark background, as I see nice design with dark background in the contest.

Thank you

I am going to develop a Mobile App (Android & IOS) for payment/e-wallet project (Tessa Hub). We will use Angular 2/ Ionic 2 for the mobile/Web app. For the server we use Cyclos server with web services on swagger.

Please provides about 7 mobiles mockup and 3 websites pages Mockup.
You will find in attached : Our current logo and the layout examples for each pages.
We need good and nice designs for our App.

Bonus : if you can give a good new proposal or redesign our current logo or convert it to vector format.

We would like all the pages to match the colors chosen in the logo.

The winner will be hired to work on the rest of the project.

Please find others info : Our website : www.velmoria.site

https://files.tarnwick.net/document/d/7QpL-r52vzTk3mNa8WdYcXoHb_FeUqRsJ1tZPyGbKw/edit?usp=sharing

```html
<!DOCTYPE html>
<html lang="en">
<head>
<meta charset="utf-8">
<title>Tessa Hub – Mobile Wallet Screens</title>
<link href="https://fonts.googleapis.com/css2?family=Lato:wght@300;400;700;900&display=swap" rel="stylesheet">
<style>
:root{
  --stage:#1b2531;
  --screen:#1d3246;
  --screen-deep:#182a3c;
  --row-line:#27405a;
  --text:#e9f0f6;
  --muted:#7f96ab;
  --green:#8cc63f;
  --green-dark:#5f9f3a;
  --teal:#2f6f6d;
  --blue:#1f6fc0;
  --blue-btn:#1d66b8;
  --red:#e04b4b;
  --avatar:#c9ccd1;
}
*{box-sizing:border-box;margin:0;padding:0}
html,body{width:1200px;height:900px;overflow:hidden}
body{background:var(--stage);font-family:"Lato",sans-serif;color:var(--text)}
.board{width:1200px;height:900px;display:flex;flex-direction:column;justify-content:center;gap:20px;padding:0 24px}
.row{display:flex;justify-content:center;gap:24px}
.screen{width:270px;height:420px;background:var(--screen);border-radius:6px;overflow:hidden;position:relative;display:flex;flex-direction:column;box-shadow:0 10px 30px rgba(0,0,0,.35)}
.status{height:18px;display:flex;justify-content:flex-end;align-items:center;gap:5px;padding:0 10px;font-size:9px;color:var(--text)}
.status svg{width:9px;height:9px;fill:var(--text)}
.hero{background:linear-gradient(160deg,var(--green) 0%,var(--teal) 75%,var(--screen) 100%);position:relative}
.bar{display:flex;align-items:center;gap:10px;padding:4px 14px;font-size:14px;font-weight:700}
.bar svg{width:14px;height:14px;stroke:var(--text);fill:none;stroke-width:2}
.bar .grow{flex:1}
.avatar{border-radius:50%;background:radial-gradient(circle at 50% 40%,#e6e8eb,var(--avatar) 60%,#8f959c)}
.list-row{display:flex;align-items:center;gap:10px;padding:0 14px;border-bottom:1px solid var(--row-line);font-size:11px}
.list-row .grow{flex:1}
.chev{width:8px;height:8px;stroke:var(--muted);fill:none;stroke-width:2}
.icon{width:16px;height:16px;stroke:var(--green);fill:none;stroke-width:1.6}
.btn{border:none;color:#fff;font-family:inherit;font-weight:700;display:flex;align-items:center;justify-content:center;gap:6px}
.btn-green{background:var(--green)}
.btn-blue{background:var(--blue-btn)}
.btn-red{background:var(--red)}
.sm{font-size:8px;color:var(--muted)}
.plus{color:#fff;font-weight:700}
.minus{color:#fff}

/* filter */
.pills{display:flex;gap:6px;justify-content:center;padding:6px 0 2px}
.pill{font-size:8px;padding:3px 10px;border-radius:10px;border:1px solid rgba(255,255,255,.4)}
.pill.on{background:var(--green);border-color:var(--green)}
.tx{height:40px}
.tx .name{font-size:10px;font-weight:700}
.tx .avatar{width:22px;height:22px;flex:none}

/* menu */
.menu{padding-top:10px}
.menu .list-row{height:38px;border:none;font-size:11px;color:#d3dde6}
.menu-close{align-self:flex-end;padding:6px 14px;color:var(--muted);font-size:14px}

/* activity */
.activity-total{text-align:center;font-size:18px;font-weight:700;margin-top:2px}
.activity-sub{text-align:center;font-size:8px;opacity:.85}
.tag{display:inline-block;background:var(--green);color:#1d3246;font-size:8px;font-weight:700;padding:2px 8px;border-radius:9px}

/* home */
.home-hero{height:150px;padding:0 14px}
.home-tag{display:inline-block;background:var(--green);font-size:8px;padding:2px 6px;border-radius:2px}
.balance{font-size:24px;font-weight:900;letter-spacing:.5px}
.home-actions{display:flex;gap:8px;margin-top:8px}
.home-actions .btn{flex:1;height:26px;font-size:9px;border-radius:2px}
.home .list-row{height:44px}

/* profile */
.profile-hero{height:120px}
.profile-body{text-align:center;padding:0 22px}
.lorem{font-size:8px;line-height:1.5;color:#b8c6d3;margin-top:8px}
.profile-actions{display:flex;gap:10px;padding:14px 20px}
.profile-actions .btn{flex:1;height:28px;font-size:9px;border-radius:2px}

/* send */
.modes{display:flex;justify-content:space-between;align-items:flex-start;padding:8px 12px}
.mode{display:flex;flex-direction:column;align-items:center;gap:4px;font-size:7px;color:var(--muted);width:44px;text-align:center}
.mode .ring{width:30px;height:30px;border-radius:50%;border:1px solid var(--muted);display:flex;align-items:center;justify-content:center}
.mode .ring svg{width:14px;height:14px;stroke:var(--muted);fill:none;stroke-width:1.5}
.mode.on .ring{background:var(--green);border-color:var(--green);width:36px;height:36px}
.mode.on .ring svg{stroke:#fff}
.mode.on{color:var(--green)}
.field{padding:8px 16px;border-bottom:1px solid var(--row-line)}
.field-label{font-size:10px;color:var(--green)}
.field-value{font-size:15px;font-weight:700;display:flex;align-items:center;gap:8px;margin-top:3px}
.field-value .unit{margin-left:auto;font-size:11px;color:var(--muted);font-weight:400}
.big{font-size:24px}
.stack{margin-top:auto}
.stack .btn{width:100%;height:40px;font-size:11px;letter-spacing:.5px}
.cancel{height:34px;display:flex;align-items:center;justify-content:center;font-size:10px;background:var(--screen-deep);color:#c5d2dd}

/* add contact */
.form-top{display:flex;align-items:center;padding:6px 14px;font-size:16px;color:#fff}
.form-title{text-align:center;font-size:10px;color:#c5d2dd}
.upload{width:72px;height:72px;border-radius:50%;border:3px solid var(--green);margin:10px auto;display:flex;align-items:center;justify-content:center;color:var(--green);font-size:24px;background:var(--screen-deep)}
.input{margin:0 22px;height:38px;border-bottom:1px solid var(--row-line);display:flex;align-items:center;justify-content:center;font-size:10px;color:#c5d2dd}
</style>
</head>
<body>
<main class="board">

<div class="row">

  <!-- Filter -->
  <section class="screen">
    <div class="hero" style="height:150px">
      <div class="status"><svg viewBox="0 0 10 10"><rect x="0" y="2" width="10" height="7"/></svg>12:30</div>
      <div class="bar">
        <svg viewBox="0 0 16 16"><path d="M3 4h10M3 8h10M3 12h10"/></svg>
        <span class="grow" style="font-size:12px">Filter</span>
        <svg viewBox="0 0 16 16"><path d="M4 4l8 8M12 4l-8 8"/></svg>
      </div>
      <div class="pills"><span class="pill">All</span><span class="pill on">Received</span><span class="pill">Sent</span></div>
      <svg viewBox="0 0 270 70" width="270" height="70" style="display:block">
        <path d="M0 50 C40 30 70 60 110 38 S180 20 220 34 S260 28 270 24" stroke="rgba(255,255,255,.55)" stroke-width="1.5" fill="none"/>
      </svg>
    </div>
    <div class="list-row tx"><div class="avatar" role="img" aria-label="Contact photo"></div><div class="grow"><div class="name">Aren Tavitian</div><div class="sm">Payment</div></div><span class="plus">+55 HTG</span></div>
    <div class="list-row tx"><div class="avatar" role="img" aria-label="Contact photo"></div><div class="grow"><div class="name">Dorian Mercer</div><div class="sm">Payment</div></div><span class="minus">-55 HTG</span></div>
    <div class="list-row tx"><div class="avatar" role="img" aria-label="Contact photo"></div><div class="grow"><div class="name">Nadia Lorne</div><div class="sm">Payment</div></div><span class="plus">+55 HTG</span></div>
    <div class="list-row tx"><div class="avatar" role="img" aria-label="Contact photo"></div><div class="grow"><div class="name">Rupert Hale</div><div class="sm">Payment</div></div><span class="minus">-55 HTG</span></div>
    <div class="list-row tx"><div class="avatar" role="img" aria-label="Contact photo"></div><div class="grow"><div class="name">Aren Tavitian</div><div class="sm">Payment</div></div><span class="plus">+55 HTG</span></div>
  </section>

  <!-- Menu -->
  <section class="screen menu" style="background:var(--screen-deep)">
    <div class="status">12:30</div>
    <div class="menu-close">✕</div>
    <div class="list-row"><svg class="icon" viewBox="0 0 16 16"><path d="M2 8l6-5 6 5v6H2z"/></svg>Home</div>
    <div class="list-row"><svg class="icon" viewBox="0 0 16 16"><path d="M2 14l12-6L2 2l2 6z"/></svg>My Receivers</div>
    <div class="list-row"><svg class="icon" viewBox="0 0 16 16"><rect x="2" y="4" width="12" height="9"/><path d="M2 7h12"/></svg>My Bank Accounts</div>
    <div class="list-row"><svg class="icon" viewBox="0 0 16 16"><path d="M3 3h10v10H3zM6 8h4"/></svg>My Requests</div>
    <div class="list-row"><svg class="icon" viewBox="0 0 16 16"><rect x="2" y="2" width="5" height="5"/><rect x="9" y="2" width="5" height="5"/><rect x="2" y="9" width="5" height="5"/></svg>Show my QR Code</div>
    <div class="list-row"><svg class="icon" viewBox="0 0 16 16"><path d="M3 13l2-5 6-6 3 3-6 6z"/></svg>Edit Profile</div>
    <div class="list-row"><svg class="icon" viewBox="0 0 16 16"><circle cx="8" cy="8" r="3"/><circle cx="8" cy="8" r="6"/></svg>Settings</div>
  </section>

  <!-- Activity -->
  <section class="screen">
    <div class="hero" style="height:165px">
      <div class="status">12:30</div>
      <div class="bar">
        <svg viewBox="0 0 16 16"><path d="M14 8H3M7 4L3 8l4 4"/></svg>
        <span class="grow">Activity</span>
        <svg viewBox="0 0 16 16"><path d="M3 4h10M3 8h10M3 12h10"/></svg>
      </div>
      <div style="padding:2px 14px"><span class="tag">1 Year</span></div>
      <div class="activity-total">2730 HTG</div>
      <div class="activity-sub">Total expense: AUG 12 - SEP 12</div>
      <svg viewBox="0 0 270 60" width="270" height="60" style="display:block">
        <path d="M0 45 C40 50 70 20 120 30 S190 10 230 18 S260 12 270 10 V60 H0Z" fill="rgba(255,255,255,.12)"/>
        <path d="M0 45 C40 50 70 20 120 30 S190 10 230 18 S260 12 270 10" stroke="#fff" stroke-width="1.5" fill="none"/>
        <circle cx="230" cy="18" r="3.5" fill="#fff"/>
      </svg>
    </div>
    <div class="list-row tx"><div class="avatar" role="img" aria-label="Contact photo"></div><div class="grow"><div class="name">Aren Tavitian</div><div class="sm">Payment · 12.07.2017</div></div><span class="minus">-55 HTG</span></div>
    <div class="list-row tx"><div class="avatar" role="img" aria-label="Contact photo"></div><div class="grow"><div class="name">Dorian Mercer</div><div class="sm">Payment · 12.07.2017</div></div><span class="plus">+55 HTG</span></div>
    <div class="list-row tx"><div class="avatar" role="img" aria-label="Contact photo"></div><div class="grow"><div class="name">Nadia Lorne</div><div class="sm">Payment · 12.07.2017</div></div><span class="plus">+55 HTG</span></div>
    <div class="list-row tx"><div class="avatar" role="img" aria-label="Contact photo"></div><div class="grow"><div class="name">Rupert Hale</div><div class="sm">Payment · 12.07.2017</div></div><span class="minus">-55 HTG</span></div>
    <div class="list-row tx"><div class="avatar" role="img" aria-label="Contact photo"></div><div class="grow"><div class="name">Aren Tavitian</div><div class="sm">Payment · 12.07.2017</div></div><span class="minus">-55 HTG</span></div>
  </section>

  <!-- Home -->
  <section class="screen home">
    <div class="hero home-hero">
      <div class="status" style="padding:0">12:30</div>
      <div style="display:flex;justify-content:space-between;align-items:flex-start">
        <div>
          <svg viewBox="0 0 16 16" width="14" height="14" style="stroke:#fff;stroke-width:2"><path d="M2 4h12M2 8h12M2 12h12"/></svg>
          <div style="margin-top:4px"><span class="home-tag">Personal Account</span></div>
          <div style="font-size:10px;margin-top:6px">Manage Balance</div>
          <div class="balance">104,53 HTG</div>
          <div style="font-size:9px;font-weight:700">See Activity ›</div>
        </div>
        <div style="text-align:center">
          <div class="avatar" role="img" aria-label="User photo" style="width:40px;height:40px;border:2px solid #fff"></div>
          <div style="font-size:9px;margin-top:4px">John Doe</div>
        </div>
      </div>
      <div class="home-actions">
        <button class="btn btn-green">Send Money</button>
        <button class="btn btn-blue">Request Money</button>
      </div>
    </div>
    <div class="list-row"><svg class="icon" viewBox="0 0 16 16"><circle cx="7" cy="7" r="4"/><path d="M10 10l4 4"/></svg><span class="grow">Search Agent</span><svg class="chev" viewBox="0 0 8 8"><path d="M2 1l3 3-3 3"/></svg></div>
    <div class="list-row"><svg class="icon" viewBox="0 0 16 16"><rect x="3" y="2" width="10" height="12"/><circle cx="8" cy="7" r="2"/></svg><span class="grow">Contacts</span><svg class="chev" viewBox="0 0 8 8"><path d="M2 1l3 3-3 3"/></svg></div>
    <div class="list-row"><svg class="icon" viewBox="0 0 16 16"><rect x="2" y="4" width="12" height="8"/><path d="M2 7h12"/></svg><span class="grow">Mobile ATM</span><svg class="chev" viewBox="0 0 8 8"><path d="M2 1l3 3-3 3"/></svg></div>
    <div class="list-row"><svg class="icon" viewBox="0 0 16 16"><rect x="2" y="3" width="12" height="10"/><path d="M5 8h6"/></svg><span class="grow">Pay Bill</span><svg class="chev" viewBox="0 0 8 8"><path d="M2 1l3 3-3 3"/></svg></div>
    <div class="list-row"><svg class="icon" viewBox="0 0 16 16"><path d="M3 6h10l-3-3M13 10H3l3 3"/></svg><span class="grow">Transfer to Bank</span><svg class="chev" viewBox="0 0 8 8"><path d="M2 1l3 3-3 3"/></svg></div>
  </section>

</div>

<div class="row">

  <!-- User Profile -->
  <section class="screen">
    <div class="hero profile-hero">
      <div class="status">12:30</div>
      <div class="bar">
        <svg viewBox="0 0 16 16"><path d="M14 8H3M7 4L3 8l4 4"/></svg>
        <span class="grow">User Profile</span>
      </div>
    </div>
    <div class="profile-body">
      <div class="avatar" role="img" aria-label="User photo" style="width:64px;height:64px;margin:-40px auto 0;border:3px solid #fff"></div>
      <div style="font-size:15px;font-weight:700;margin-top:8px">John Doe</div>
      <p class="lorem">Member since 2017. Sends and receives payments with friends and agents. Prefers mobile transfers and quick bill payments. Contact saved in your list.</p>
    </div>
    <div class="profile-actions">
      <button class="btn btn-green">Send Money</button>
      <button class="btn btn-blue">Request Money</button>
    </div>
    <button class="btn btn-red" style="margin-top:auto;height:52px;font-size:10px">Remove From Contact</button>
  </section>

  <!-- Send Money -->
  <section class="screen">
    <div class="status">12:30</div>
    <div class="bar">
      <svg viewBox="0 0 16 16"><rect x="2" y="5" width="12" height="8"/><path d="M8 2v6"/></svg>
      <span class="grow" style="font-size:12px">Send Money</span>
      <span style="color:var(--muted)">✕</span>
    </div>
    <div class="modes">
      <div class="mode"><span class="ring"><svg viewBox="0 0 16 16"><rect x="3" y="3" width="10" height="10"/></svg></span>Scan Bar Code</div>
      <div class="mode on"><span class="ring"><svg viewBox="0 0 16 16"><circle cx="8" cy="6" r="3"/><path d="M3 14c1-3 9-3 10 0"/></svg></span>To User</div>
      <div class="mode"><span class="ring"><svg viewBox="0 0 16 16"><rect x="4" y="2" width="8" height="12"/></svg></span>To Contact</div>
      <div class="mode"><span class="ring"><svg viewBox="0 0 16 16"><rect x="2" y="4" width="12" height="8"/><path d="M2 4l6 5 6-5"/></svg></span>To Email</div>
      <div class="mode"><span class="ring" style="width:20px;height:20px;color:var(--muted)">+</span></div>
    </div>
    <div class="field">
      <div class="field-label">To</div>
      <div class="field-value"><span class="avatar" role="img" aria-label="Recipient photo" style="width:24px;height:24px;border-radius:4px"></span>Aren Tavitian<span class="unit">HTG</span></div>
    </div>
    <div class="field">
      <div class="field-label">Amount</div>
      <div class="field-value big">102,98</div>
    </div>
    <div class="field" style="border:none">
      <div class="field-label">Description</div>
      <div class="field-value">Demo Payment</div>
    </div>
    <div class="stack">
      <button class="btn btn-blue">MAKE PAYMENT</button>
      <div class="cancel">CANCEL</div>
    </div>
  </section>

  <!-- Add Contact -->
  <section class="screen">
    <div class="status">12:30</div>
    <div class="form-top">✕</div>
    <div class="form-title">Add Image</div>
    <div class="upload">+</div>
    <div class="input">Name</div>
    <div class="input">Email</div>
    <div class="input">Phone number</div>
    <div class="input">Gender ⌄</div>
    <div class="stack"><button class="btn btn-blue" style="height:46px">NEXT</button></div>
  </section>

</div>
</main>
</body>
</html>
```